Business card for law firm

Need business card for new law firm. Think confident, authoritative, conservative, but not stuffy or old-fashioned.

Contact Information for Business Card

Content for card - logo (uploaded), plus the following:

Paul Wexbury (larger font)
Managing Partner (larger font, but not as large as name)
Level 9, 41 Tansy Lane
Sydney NSW 2000
Main Tel 02 7346 2190
Direct Tel 02 6273 4415
Email paul@qvlegal.com.au
www.qvlegal.com.au

Letterhead design should include logo plus:
Level 9, 41 Tansy Lane
Sydney NSW 2000
Tel 02 6273 4415
www.qvlegal.com.au

```html
<!DOCTYPE html>
<html lang="en">
<head>
<meta charset="utf-8">
<title>Quayvale Legal – Business Card</title>
<link href="https://fonts.googleapis.com/css2?family=Cinzel:wght@400;500&family=Open+Sans:wght@400&display=swap" rel="stylesheet">
<style>
  :root {
    --backdrop: #5c5c5e;
    --card-white: #ffffff;
    --navy: #0f1c56;
    --navy-deep: #0b1648;
    --ink: #1c1c1c;
    --rule: #c9ccd6;
  }
  * { margin: 0; padding: 0; box-sizing: border-box; }
  html, body { width: 1200px; height: 802px; overflow: hidden; }
  body { background: var(--backdrop); position: relative; }

  .card {
    position: absolute;
    top: 274px;
    width: 443px;
    height: 264px;
    box-shadow: 2px 3px 6px rgba(0,0,0,0.45);
  }
  .card--front { left: 136px; background: var(--card-white); }
  .card--back { left: 624px; background: var(--navy); overflow: hidden; }

  /* front: brand column */
  .brand {
    position: absolute;
    left: 20px;
    top: 76px;
    width: 200px;
    display: flex;
    flex-direction: column;
    align-items: center;
  }
  .brand__mark {
    width: 40px;
    height: 40px;
    background: var(--navy);
    margin-bottom: 30px;
  }
  .brand__name {
    font-family: 'Cinzel', serif;
    font-weight: 400;
    font-size: 22px;
    letter-spacing: 0.5px;
    color: var(--ink);
    white-space: nowrap;
  }

  .divider {
    position: absolute;
    left: 231px;
    top: 67px;
    width: 1px;
    height: 130px;
    background: var(--rule);
  }

  /* front: contact column */
  .contact {
    position: absolute;
    left: 246px;
    top: 64px;
    font-family: 'Open Sans', sans-serif;
    color: var(--ink);
  }
  .contact__name {
    font-family: 'Cinzel', serif;
    font-weight: 500;
    font-size: 18px;
    line-height: 20px;
    color: var(--navy);
    text-transform: uppercase;
    white-space: nowrap;
  }
  .contact__role { font-size: 13px; line-height: 16px; }
  .contact__lines { list-style: none; margin-top: 4px; }
  .contact__lines li {
    font-size: 13px;
    line-height: 16px;
    display: flex;
    align-items: center;
    gap: 3px;
    white-space: nowrap;
  }
  .contact__lines svg { width: 9px; height: 9px; fill: var(--navy); flex: none; }
  .contact__tag { font-size: 11px; }
  .contact__address { font-size: 13px; line-height: 16px; margin-top: 5px; font-style: normal; }

  /* back */
  .back__field {
    position: absolute;
    inset: 0;
    background: linear-gradient(180deg, #142264 0%, var(--navy) 50%, var(--navy-deep) 100%);
  }
  .back__name {
    position: absolute;
    left: 0;
    right: 0;
    top: 112px;
    text-align: center;
    font-family: 'Cinzel', serif;
    font-weight: 400;
    font-size: 30px;
    letter-spacing: 1px;
    color: var(--card-white);
  }
</style>
</head>
<body>
  <section class="card card--front" aria-label="Business card front">
    <div class="brand">
      <span class="brand__mark" aria-hidden="true"></span>
      <span class="brand__name">Quayvale Legal</span>
    </div>

    <span class="divider" aria-hidden="true"></span>

    <div class="contact">
      <h1 class="contact__name">Paul Wexbury</h1>
      <p class="contact__role">Managing Partner</p>
      <ul class="contact__lines">
        <li><svg viewBox="0 0 10 10" aria-hidden="true"><path d="M1 3.5C1 2 2.5 1.5 5 1.5S9 2 9 3.5L7.4 4 7 3H3l-.4 1zM2.5 5h5l1 3.5h-7z"/></svg>02 7346 2190</li>
        <li><svg viewBox="0 0 10 10" aria-hidden="true"><path d="M1 3.5C1 2 2.5 1.5 5 1.5S9 2 9 3.5L7.4 4 7 3H3l-.4 1zM2.5 5h5l1 3.5h-7z"/></svg>02 6273 4415 <span class="contact__tag">(DIRECT)</span></li>
        <li><svg viewBox="0 0 10 10" aria-hidden="true"><path d="M1 2h8v6H1zM1.6 2.6 5 5.4l3.4-2.8v.8L5 6.2 1.6 3.4z" fill-rule="evenodd"/></svg>paul@qvlegal.com.au</li>
        <li><svg viewBox="0 0 10 10" aria-hidden="true"><circle cx="5" cy="5" r="4.2"/></svg>www.qvlegal.com.au</li>
      </ul>
      <address class="contact__address">Level 9, 41 Tansy Lane<br>Sydney NSW 2000</address>
    </div>
  </section>

  <section class="card card--back" aria-label="Business card back">
    <div class="back__field" role="img" aria-label="Navy field with a faint repeating brand-symbol pattern"></div>
    <p class="back__name">QUAYVALE LEGAL</p>
  </section>
</body>
</html>
```